依頼概要
ふわりやと言うめろんぱんチェンーのキャンペーン商品のポスター依頼です。
昨年も販売した商品で今年も6月から期間限定で販売します。
商品名 小春ミントメロンパン
売価  320円
サイズ B2
ポスターに求める事は、夏場の暑い時期に見ても、さっぱりした感じのするポスターをお願いしたいと思います。店舗と商品のイメージはHPをご覧になって下さい。
ファイルは、そのままネット印刷会社に依頼できる状態のファイルとCS2で編集可能なアウトライン前のファイルと出して頂ける事を条件とします。

瀬戸内のブランドイメージの表現と夏の感じが強く感じられ、商品も遠目から瞬間的に認識で、訴求につながると選考したスッタフの意見となりました。

沢山のご応募頂き有難うございました。
最終の選考に5人の方を絞り、いずれもお願いしたいくらい素晴らし作品でした。また次は、秋の商品・新商品を検討しております。
今後とも宜しくお願い致します。

```html
<!DOCTYPE html>
<html lang="ja">
<head>
<meta charset="utf-8">
<title>小春ミントメロンパン 期間限定ポスター</title>
<link rel="stylesheet" href="https://fonts.googleapis.com/css2?family=M+PLUS+Rounded+1c:wght@500;800&display=swap">
<style>
  :root {
    --sky: #4ea6da;
    --paper: #ffffff;
    --lemon-pale: #f7e68e;
    --lemon: #f3d95e;
    --bread-light: #f2d27a;
    --bread-mid: #e8bb5e;
    --bread-dark: #c98a3a;
    --ink-brown: #7a4a2a;
  }
  * { margin: 0; padding: 0; box-sizing: border-box; }
  html, body { width: 846px; height: 1200px; overflow: hidden; background: var(--paper); }
  .poster {
    position: relative;
    width: 846px;
    height: 1200px;
    overflow: hidden;
    background: var(--paper);
    font-family: "M PLUS Rounded 1c", sans-serif;
    color: var(--sky);
  }
  .label-limited {
    position: absolute; left: 52px; top: 32px;
    font-size: 36px; font-weight: 800; letter-spacing: 2px; line-height: 46px;
  }
  .rule { position: absolute; left: 52px; height: 3px; background: var(--sky); }
  .rule.r1 { top: 82px; width: 360px; }
  .rule.r2 { top: 184px; width: 500px; }
  .rule.r3 { top: 262px; width: 560px; }
  .product-name {
    position: absolute; left: 52px; top: 100px;
    font-size: 62px; font-weight: 800; line-height: 80px; letter-spacing: 4px;
  }
  .visual-bubble {
    position: absolute; left: 530px; top: 30px; width: 290px; height: 250px;
  }
  .description {
    position: absolute; left: 52px; top: 284px;
    font-size: 29px; font-weight: 800; line-height: 46px; letter-spacing: 1px;
  }
  .price {
    position: absolute; left: 52px; top: 468px;
    display: flex; align-items: center; font-weight: 800;
  }
  .price-amount { font-size: 76px; line-height: 80px; letter-spacing: 2px; }
  .price-tax { font-size: 26px; line-height: 28px; margin-left: 8px; width: 28px; }
  .shop-name {
    position: absolute; left: 606px; top: 494px;
    display: flex; align-items: center; gap: 8px; color: var(--ink-brown);
  }
  .shop-name .mark { width: 26px; height: 26px; border-radius: 50%; background: var(--bread-light); }
  .shop-name .name { font-size: 36px; font-weight: 800; line-height: 44px; }
  .shop-tagline {
    position: absolute; left: 606px; top: 544px;
    font-size: 12px; font-weight: 500; color: var(--ink-brown);
  }
  .stripes {
    position: absolute; left: 0; top: 626px; width: 846px; height: 574px;
    background: repeating-linear-gradient(to bottom, var(--sky) 0 28px, var(--paper) 28px 56px);
  }
  .product-photo {
    position: absolute; left: 175px; top: 654px; width: 510px; height: 488px;
    border-radius: 48% 48% 42% 42% / 56% 56% 44% 44%;
    background: radial-gradient(ellipse at 45% 35%, var(--bread-light) 0%, var(--bread-mid) 60%, var(--bread-dark) 100%);
  }
</style>
</head>
<body>
<main class="poster">
  <header>
    <p class="label-limited">期間限定</p>
    <div class="rule r1"></div>
    <h1 class="product-name">小春ミント<br>メロンパン</h1>
    <div class="rule r2"></div>
    <div class="rule r3"></div>
  </header>

  <svg class="visual-bubble" viewBox="0 0 290 250" role="img" aria-label="果実の輪切りを描いた吹き出し型のイラスト">
    <defs>
      <radialGradient id="bubbleTone" cx="50%" cy="45%" r="60%">
        <stop offset="0%" stop-color="var(--lemon)"/>
        <stop offset="100%" stop-color="var(--lemon-pale)"/>
      </radialGradient>
    </defs>
    <path d="M150 5 C235 5 285 55 285 120 C285 185 235 230 155 230 C125 230 100 223 80 212 L25 240 L50 190 C30 170 15 146 15 120 C15 55 65 5 150 5 Z" fill="url(#bubbleTone)"/>
  </svg>

  <p class="description">香りが爽やかな小春ミントと<br>ホイップクリームを<br>ふわりやメロンに<br>サンドしました。</p>

  <p class="price"><span class="price-amount">¥320</span><span class="price-tax">税込</span></p>

  <div class="shop-name"><span class="mark"></span><span class="name">ふわりや</span></div>
  <p class="shop-tagline">ふわふわ焼きたて</p>

  <div class="stripes"></div>
  <div class="product-photo" role="img" aria-label="ホイップクリームをはさんだメロンパンの写真"></div>
</main>
</body>
</html>
```